New Body Mist 250 ml exclusive

We are excited to embark on a new project to design the packaging for body mist:
Amber Drizzle

We are looking for a design that is truly unique and stands out, with a touch of individuality that sets it apart. The design should be eye-catching and visually appealing, drawing attention even from a distance. We want the body mists to have a fun and attractive look that appeals to customers.

To help bring your design to life, we will provide the dimensions of the bottle, which has a capacity of 250ml. The bottle measures 13.3 cm in height and 4.9 cm in diameter (excluding the pump). Additionally, we will also provide the dimensions of the label, which measures 15.1 cm in height and 12.8 cm in width.

We believe that giving you the freedom to put your own unique touch and color choices will help create a truly standout design. We look forward to seeing your creative vision for our body mist.

We shared with you the logo of the body mist and some examples of models that we liked.

Please be informed that the project only includes one design and the remaining three will be completed and paid for through a 1on1 project with the winner of the contest.

Target Market(s)

Supermarket and perfumery stores

Industry/Entity Type

Cosmetics

Font styles to use
Serif

Requirements
Must have
• Uniqueness and attractiveness

```html
<!DOCTYPE html>
<html lang="en">
<head>
<meta charset="UTF-8">
<title>Amber Drizzle Body Mists – Label Range</title>
<link rel="stylesheet" href="https://fonts.googleapis.com/css2?family=Josefin+Sans:wght@400&family=Playfair+Display:ital,wght@1,500&family=Oswald:wght@400&display=swap">
<style>
  :root {
    --canvas: #f1eeee;
    --gold: #d9a31a;
    --gold-dark: #bb860c;
    --white: #ffffff;
    --ink: #1c1a16;
    --blue-bloom: #1f6ef0;
    --blue-light: #5aa8ff;
    --blue-deep: #0f4fc9;
    --blue-base: #1a86d6;
    --blue-low: #1670c4;
    --violet-bloom: #7a3fd8;
    --violet-light: #d27cf0;
    --violet-deep: #5a2bb8;
    --violet-base: #a58be6;
    --violet-low: #9a70e0;
    --rose-bloom: #f7cfda;
    --rose-light: #fdf2f4;
    --rose-deep: #e27d9c;
    --rose-base: #f3c9d5;
    --rose-low: #d65f8d;
  }
  * { box-sizing: border-box; margin: 0; padding: 0; }
  html, body { width: 1200px; height: 853px; overflow: hidden; background: var(--canvas); }
  .range {
    width: 1200px; height: 853px;
    display: flex; justify-content: center; align-items: center; gap: 64px;
  }
  .label {
    position: relative; width: 250px; height: 760px; overflow: hidden;
    border-radius: 6px; box-shadow: 0 8px 24px rgba(0,0,0,.12);
  }
  .label--iris { background: linear-gradient(180deg, var(--blue-base) 50%, var(--blue-low)); }
  .label--dew { background: linear-gradient(180deg, var(--violet-base) 50%, var(--violet-low)); }
  .label--blush { background: linear-gradient(180deg, var(--rose-base) 50%, var(--rose-low)); }
  .brand-band {
    position: relative; z-index: 2;
    height: 84px; background: linear-gradient(180deg, var(--gold), var(--gold-dark));
    display: flex; align-items: center; justify-content: center;
  }
  .brand-name {
    font-family: "Josefin Sans", sans-serif; font-weight: 400; font-size: 25px;
    color: var(--white); letter-spacing: 2px; white-space: nowrap;
  }
  .floral {
    position: absolute; left: 0; top: 84px; width: 100%; height: 420px;
    -webkit-mask-image: linear-gradient(180deg, #000 70%, transparent);
            mask-image: linear-gradient(180deg, #000 70%, transparent);
  }
  .label--iris .floral {
    background:
      radial-gradient(circle at 25% 20%, var(--blue-light), transparent 30%),
      radial-gradient(circle at 75% 12%, var(--blue-light), transparent 28%),
      radial-gradient(circle at 55% 45%, var(--blue-deep), transparent 35%),
      radial-gradient(circle at 30% 70%, var(--blue-light), transparent 30%),
      linear-gradient(180deg, var(--blue-bloom), var(--blue-base));
  }
  .label--dew .floral {
    background:
      radial-gradient(circle at 75% 18%, var(--violet-light), transparent 32%),
      radial-gradient(circle at 20% 25%, var(--violet-deep), transparent 30%),
      radial-gradient(circle at 50% 50%, var(--violet-light), transparent 30%),
      radial-gradient(circle at 25% 72%, var(--violet-deep), transparent 30%),
      linear-gradient(180deg, var(--violet-bloom), var(--violet-base));
  }
  .label--blush .floral {
    background:
      radial-gradient(circle at 30% 15%, var(--rose-deep), transparent 22%),
      radial-gradient(circle at 70% 25%, var(--rose-bloom), transparent 32%),
      radial-gradient(circle at 30% 50%, var(--rose-light), transparent 32%),
      radial-gradient(circle at 72% 70%, var(--rose-deep), transparent 22%),
      linear-gradient(180deg, var(--rose-light), var(--rose-base));
  }
  .title-group {
    position: absolute; z-index: 2; left: 10px; top: 598px; width: 280px;
    transform: rotate(-30deg); transform-origin: left top;
  }
  .variant-name {
    display: block; font-family: "Playfair Display", serif; font-style: italic; font-weight: 500;
    font-size: 38px; line-height: 1; color: var(--white); white-space: nowrap;
    text-shadow: 1px 2px 3px rgba(0,0,0,.35);
  }
  .mist-ribbon {
    display: inline-block; margin: 4px 0 0 92px; padding: 4px 18px 4px 14px;
    background: var(--gold); font-family: "Josefin Sans", sans-serif; font-weight: 400;
    font-size: 14px; letter-spacing: 3px; color: var(--ink); white-space: nowrap;
  }
  .volume {
    position: absolute; z-index: 2; right: 22px; bottom: 84px;
    font-family: "Oswald", sans-serif; font-size: 18px; color: var(--ink);
  }
</style>
</head>
<body>
<main class="range">
  <section class="label label--iris">
    <header class="brand-band"><span class="brand-name">Amber Drizzle</span></header>
    <div class="floral" role="img" aria-label="Photograph of blue forget-me-not flowers"></div>
    <div class="title-group">
      <span class="variant-name">Velvet Iris</span>
      <span class="mist-ribbon">BODY MISTS</span>
    </div>
    <span class="volume">250ml</span>
  </section>
  <section class="label label--dew">
    <header class="brand-band"><span class="brand-name">Amber Drizzle</span></header>
    <div class="floral" role="img" aria-label="Photograph of violet and lilac blossoms with sparkles"></div>
    <div class="title-group">
      <span class="variant-name">Dew Petal</span>
      <span class="mist-ribbon">BODY MISTS</span>
    </div>
    <span class="volume">250ml</span>
  </section>
  <section class="label label--blush">
    <header class="brand-band"><span class="brand-name">Amber Drizzle</span></header>
    <div class="floral" role="img" aria-label="Photograph of pink cherry blossom branch"></div>
    <div class="title-group">
      <span class="variant-name">Blush Always</span>
      <span class="mist-ribbon">BODY MISTS</span>
    </div>
    <span class="volume">250ml</span>
  </section>
</main>
</body>
</html>
```